M Website

We need a website design for a construction plant company. You may use a combination of our photos and the stock images. See the logo for company colours. It also be of great value to see moving pictures like the ones on the link: https://www.quindellworks.co.za/copy-of-about-us. See our uploaded files for content.

Target Market(s)

Construction

Number of Pages Required

5+ page

```html
<!DOCTYPE html>
<html lang="en">
<head>
<meta charset="utf-8">
<title>Kestrel Logistics &amp; Plant Hire</title>
<link rel="stylesheet" href="https://fonts.googleapis.com/css2?family=Montserrat:wght@300;400;500;600;700&family=Oswald:wght@400;500&display=swap">
<style>
:root{
  --orange:#f4a81d;
  --orange-dark:#e2961a;
  --ink:#333333;
  --muted:#6b6b6b;
  --line:#e6e6e6;
  --field:#f1f1f1;
  --white:#ffffff;
  --dark-btn:#4a4a4a;
}
*{box-sizing:border-box;margin:0;padding:0}
html,body{width:1200px;height:3659px;overflow:hidden}
body{position:relative;background:var(--white);font-family:"Montserrat",sans-serif;color:var(--ink)}
.abs{position:absolute}

/* header */
.site-header{left:0;top:0;width:1200px;height:112px;background:var(--white)}
.brand{left:88px;top:30px;display:flex;align-items:center;gap:12px}
.brand-dot{width:44px;height:44px;border-radius:50%;background:var(--orange)}
.brand-name{font-weight:700;font-size:19px;color:var(--ink);line-height:1.1}
.call-us{left:786px;top:14px;font-family:"Oswald",sans-serif;font-size:17px;color:var(--ink);display:flex;align-items:center;gap:6px}
.call-us b{color:var(--orange);font-weight:500}
.nav{left:482px;top:62px;display:flex;gap:46px;font-size:13px;font-weight:500}
.nav a{color:var(--ink);text-decoration:none}
.nav a.active{color:var(--orange)}
.btn-quote-top{left:984px;top:54px;width:128px;height:34px;border-radius:17px;background:var(--orange);color:#fff;font-size:13px;font-weight:600;display:flex;align-items:center;justify-content:center}

/* hero */
.hero{left:0;top:112px;width:1200px;height:518px;background:linear-gradient(180deg,#8aa3b8 0%,#d9b77a 38%,#b98a4f 65%,#6b4a2b 100%)}
.hero-title{left:0;top:322px;width:1200px;text-align:center;color:#fff;font-size:39px;line-height:48px;font-weight:300}
.hero-title b{font-weight:700}
.hero-dots{left:1097px;top:335px;display:flex;flex-direction:column;gap:8px}
.hero-dots span{width:12px;height:12px;border-radius:50%;border:2px solid #fff}
.hero-dots span.on{background:#fff}
.hero-arrow{left:592px;top:548px}

/* section headings */
.sec-title{font-size:41px;font-weight:400;color:var(--ink)}
.sec-title b{font-weight:700}
.underline{width:130px;height:2px;background:var(--orange)}
.btn-outline{height:32px;border:1.5px solid var(--orange);border-radius:16px;color:var(--orange);font-size:12px;font-weight:600;display:flex;align-items:center;justify-content:center}

/* about */
.about-title{left:88px;top:700px}
.about-line{left:88px;top:756px}
.about-lead{left:88px;top:786px;width:440px;font-size:23px;line-height:28px;color:var(--muted);font-weight:400}
.about-copy{left:615px;top:706px;width:497px;font-size:13.5px;line-height:19px;color:var(--muted)}
.about-copy p+p{margin-top:16px}
.about-copy b{color:var(--orange)}
.about-copy strong{color:var(--ink);font-weight:600}
.about-btn{left:615px;top:914px;width:130px}

/* service tiles */
.tiles{left:0;top:1025px;width:1200px;height:305px;display:flex}
.tile{position:relative;width:300px;height:305px}
.tile-label{position:absolute;left:40px;bottom:30px;color:#fff;font-size:15px;font-weight:600}
.tile.road{background:linear-gradient(160deg,#6d6a66,#2b2b2b)}
.tile.water{background:linear-gradient(160deg,#4c4f55,#25272b)}
.tile.sanitation{background:linear-gradient(160deg,#3b3f44,#1d1f22)}
.tile.housing{background:linear-gradient(160deg,#b4573f 0%,#d8d0c1 40%,#3a3a3a 100%)}
.tile-overlay{position:absolute;left:0;top:0;width:300px;height:305px;background:rgba(25,25,25,.78);padding:120px 40px 0}
.tile-overlay h4{color:#fff;font-size:15px;font-weight:600;margin-bottom:22px}
.tile-overlay p{color:#dcdcdc;font-size:12.5px;line-height:17px}
.tile-overlay span{display:block;margin-top:20px;color:var(--orange);font-size:12px;font-weight:600}

/* why choose */
.why-title{left:88px;top:1395px}
.why-line{left:88px;top:1452px}
.why-lead{left:88px;top:1490px;width:380px;font-size:18px;line-height:23px;color:var(--muted)}
.why-btn{left:88px;top:1567px;width:130px}
.values{left:615px;top:1407px;width:497px;list-style:none}
.values li{border-top:1px solid var(--line);padding:10px 0 10px 0;font-size:14px;font-weight:600;color:var(--ink)}
.values li:last-child{border-bottom:1px solid var(--line)}
.values li i{display:inline-block;width:12px;height:12px;border-radius:50%;border:3px solid var(--orange);margin:0 12px 0 4px;vertical-align:-1px}
.values li p{font-weight:400;font-size:12px;color:var(--muted);margin:6px 0 0 28px}

/* commitment band */
.band{left:0;top:1762px;width:1200px;height:283px;background:linear-gradient(180deg,rgba(244,168,29,.92),rgba(230,154,22,.95)),linear-gradient(110deg,#c48c1e,#8b6a34)}
.band-title{left:0;top:1823px;width:1200px;text-align:center;color:#fff;font-size:37px;line-height:46px;font-weight:300}
.band-title b{font-weight:700}
.band-btn{left:537px;top:1940px;width:126px;height:34px;border-radius:17px;background:var(--dark-btn);color:#fff;font-size:12px;font-weight:600;display:flex;align-items:center;justify-content:center}

/* projects */
.projects-title{left:0;top:2112px;width:1200px;text-align:center}
.proj{position:absolute}
.p1{left:88px;top:2217px;width:417px;height:239px;background:linear-gradient(160deg,#7fa7d8,#c7a84a 55%,#5a4b36)}
.p2{left:537px;top:2217px;width:270px;height:239px;background:linear-gradient(160deg,#6a8f4c,#2e2e2e 60%,#3c3c3c)}
.p3{left:841px;top:2217px;width:271px;height:239px;background:linear-gradient(180deg,#9ec0e6,#8c8f7a 45%,#2d2d2d 80%)}
.p4{left:88px;top:2488px;width:271px;height:239px;background:linear-gradient(180deg,#7fb2e8,#4d4d4d 50%,#232323)}
.p5{left:390px;top:2488px;width:273px;height:239px;background:linear-gradient(180deg,#2a3e5a,#3a3a3a 60%,#202020)}
.p6{left:695px;top:2488px;width:417px;height:239px;background:linear-gradient(160deg,#8aa0b8,#a07b52 50%,#5b4a33)}
.projects-btn{left:528px;top:2767px;width:144px}

/* map */
.map{left:0;top:2818px;width:1200px;height:345px;background:linear-gradient(135deg,#e9e9e9,#dedede)}
.map-pin{left:585px;top:2960px}

/* contact */
.contact-title{left:88px;top:3232px}
.contact-line{left:88px;top:3288px}
.contact-info{left:88px;top:3322px;font-size:12.5px;color:var(--ink)}
.help{font-weight:600}
.phone{font-family:"Oswald",sans-serif;font-size:37px;color:var(--orange);margin-top:6px;line-height:42px}
.email{margin-top:4px}
.email b{color:var(--ink)}
.offices{margin-top:20px;display:flex;gap:26px;font-weight:600}
.offices .on{color:var(--orange);border-bottom:1.5px solid var(--orange)}
.address{margin-top:14px;line-height:30px;color:var(--muted)}
.field{position:absolute;background:var(--field);font-size:12px;color:var(--muted);padding:12px 14px}
.f-name{left:615px;top:3244px;width:241px;height:41px}
.f-phone{left:871px;top:3244px;width:241px;height:41px}
.f-email{left:615px;top:3303px;width:497px;height:41px}
.f-msg{left:615px;top:3361px;width:497px;height:132px}
.send{left:1046px;top:3476px;width:40px;height:40px;border-radius:50%;background:var(--orange);display:flex;align-items:center;justify-content:center}
.footer{left:0;top:3577px;width:1200px;text-align:center;font-size:12px;color:var(--muted)}
.footer b{color:var(--orange)}
</style>
</head>
<body>

<header class="abs site-header">
  <div class="abs brand"><span class="brand-dot"></span><span class="brand-name">Kestrel</span></div>
  <div class="abs call-us">Call Us
    <svg width="16" height="16" viewBox="0 0 24 24"><circle cx="12" cy="12" r="12" fill="#f4a81d"/><path d="M8 6l2 0 1 3-1.5 1a8 8 0 0 0 4.5 4.5l1-1.5 3 1 0 2c0 1-1 2-2 2A11 11 0 0 1 6 8c0-1 1-2 2-2z" fill="#fff"/></svg>
    <b>+27 (0) 10 555 0142</b></div>
  <nav class="abs nav"><a class="active">Home</a><a>About Us</a><a>Services</a><a>Projects</a><a>Contact Us</a></nav>
  <div class="abs btn-quote-top">Get a quote</div>
</header>

<section class="abs hero" role="img" aria-label="Excavator digging earth at a construction site under a sunset sky"></section>
<h1 class="abs hero-title"><b>Transforming</b> Our Clients<br><b>Vision</b> Into <b>Reality</b></h1>
<div class="abs hero-dots"><span class="on"></span><span></span><span></span><span></span></div>
<svg class="abs hero-arrow" width="16" height="24" viewBox="0 0 16 24"><path d="M8 2v18M3 15l5 5 5-5" stroke="#fff" stroke-width="2" fill="none"/></svg>

<h2 class="abs sec-title about-title">About <b>Us</b></h2>
<div class="abs underline about-line"></div>
<p class="abs about-lead">Delivering high quality multidisciplinary engineering &amp; construction projects</p>
<div class="abs about-copy">
  <p><b>Kestrel</b> <strong>Logistics and Plant Hire</strong> (Pty) Ltd is a Black Woman owned Construction and Plant Hire company operating mainly from the Kestrel head office in Midrand (Kleinfontein) Gauteng. Kestrel Logistics and Plant Hire (Pty) Ltd was established in 2014, and has worked in various municipal jurisdictions within South Africa.</p>
  <p>Since inception, Kestrel Logistics and Plant Hire (Pty) Ltd has worked on a number of projects, acquiring a track record primarily in the following disciplines, amongst the company's offerings and/ or services ...</p>
</div>
<div class="abs btn-outline about-btn">Discover more</div>

<section class="abs tiles">
  <div class="tile road" role="img" aria-label="Workers laying asphalt on a road"><span class="tile-label">Roads &amp; Stormwater</span></div>
  <div class="tile water" role="img" aria-label="Large water pipes being installed"><span class="tile-label">Water Infrastructure</span></div>
  <div class="tile sanitation" role="img" aria-label="Sanitation infrastructure works">
    <div class="tile-overlay"><h4>Sanitation Infrastructure</h4><p>Upgrade of Infrastructure – Eradication of bucket systems The projects descriptions ...</p><span>Discover more</span></div>
  </div>
  <div class="tile housing" role="img" aria-label="Paved driveway beside a new house"><span class="tile-label" style="left:120px">Housing</span></div>
</section>

<h2 class="abs sec-title why-title">Why Choose <b>Us</b></h2>
<div class="abs underline why-line"></div>
<p class="abs why-lead">We are committed to achieving this through the following:</p>
<div class="abs btn-outline why-btn">Get a quote</div>
<ul class="abs values">
  <li><i></i>Integrity</li>
  <li><i></i>Accountability<p>Providing a service to our Clients which meets their expectations.</p></li>
  <li><i></i>Reliability</li>
  <li><i></i>Capability</li>
  <li><i></i>Adaptability</li>
  <li><i></i>Ethics</li>
</ul>

<section class="abs band" role="img" aria-label="Freshly surfaced road tinted in company orange"></section>
<h2 class="abs band-title">Our Commitment to <b>Safety, Quality</b> and<br>the <b>Environment</b> is Paramount.</h2>
<div class="abs band-btn">Contact Us</div>

<h2 class="abs sec-title projects-title">Our <b>Projects</b></h2>
<div class="proj p1" role="img" aria-label="Tipper truck and paver at a road project"></div>
<div class="proj p2" role="img" aria-label="Road roller compacting new asphalt"></div>
<div class="proj p3" role="img" aria-label="Paving a circular area in a residential street"></div>
<div class="proj p4" role="img" aria-label="Asphalt paver with worker on site"></div>
<div class="proj p5" role="img" aria-label="Night road works with paving machine"></div>
<div class="proj p6" role="img" aria-label="Workers in safety vests at a trench"></div>
<div class="abs btn-outline projects-btn">View all projects</div>

<section class="abs map" role="img" aria-label="Street map showing the office location"></section>
<svg class="abs map-pin" width="30" height="40" viewBox="0 0 30 40"><path d="M15 0a14 14 0 0 0-14 14c0 10 14 26 14 26s14-16 14-26A14 14 0 0 0 15 0z" fill="#f4a81d"/><circle cx="15" cy="14" r="5" fill="#fff"/></svg>

<h2 class="abs sec-title contact-title">Contact <b>Us</b></h2>
<div class="abs underline contact-line"></div>
<div class="abs contact-info">
  <div class="help">Need Help? Call Us</div>
  <div class="phone">+27 (0) 10 555 0142</div>
  <div class="email"><b>E:</b> info@kestrelplant.co.za</div>
  <div class="offices"><span class="on">Headoffice</span><span>Free State office</span></div>
  <div class="address">P.O Box 318, Hillcrest Park, 1690 12 Acacia Lane,<br>Kleinfontein, Midrand, 1692</div>
</div>
<div class="field f-name">Name</div>
<div class="field f-phone">Phone</div>
<div class="field f-email">Email</div>
<div class="field f-msg">Message</div>
<div class="abs send"><svg width="16" height="16" viewBox="0 0 16 16"><path d="M3 8h10M9 4l4 4-4 4" stroke="#fff" stroke-width="2" fill="none"/></svg></div>

<footer class="abs footer">© 2019 <b>Kestrel</b> Logistics &amp; Plant Hire. All right reserved</footer>

</body>
</html>
```